Digital Product Store Front for Educational Leaders (PraisewithPellar)

I am an a Principal, Author and Education consultant I am in need of a wordpress website that fits my brand that I will be able to sell digital products I have created, digital courses I have created, and offer mentorship and coaching services. I have my branding documents and my content/wording in the files. This website should be professional yet relatable. I'd like it to be clean, easy to navigate and be very obvious with its purpose. Please view the attached documents to give a much clearer idea about my brand and wants. :)

Target Market(s)

Educational Leaders (Principals)

Industry/Entity Type

Educational Leadership

Coding

Coded - Design and coding required

Number of Pages Required

1 page

Font styles to use
Other font styles liked:
• please use my branding font

Requirements
Must have
• All the items I listed on my document, my brand colors and font, The content I submitted is still in a very draft format but just to give the designer and idea.

```html
<!DOCTYPE html>
<html lang="en">
<head>
<meta charset="utf-8">
<title>PraisewithPellar</title>
<link rel="stylesheet" href="https://fonts.googleapis.com/css2?family=Barlow:wght@300;400;500&family=IBM+Plex+Mono:ital,wght@0,400;0,500;1,600&display=swap">
<style>
:root{
  --teal:#5b9a8f;
  --teal-soft:#73a79e;
  --teal-deep:#0f5446;
  --sand:#f4efe6;
  --mist:#f3f3f1;
  --ink:#3a3a3a;
  --cream:#f1e3c0;
  --white:#ffffff;
}
*{margin:0;padding:0;box-sizing:border-box}
html,body{width:1200px;height:5206px;overflow:hidden}
body{position:relative;background:var(--white);color:var(--ink);font-family:"IBM Plex Mono",monospace;font-size:13.5px;line-height:1.62}
.abs{position:absolute}
.heading{font-family:"Barlow",sans-serif;font-weight:300;color:var(--teal);letter-spacing:1px;line-height:1.2}
.copy{font-size:13.5px;color:var(--ink)}
.copy em{font-style:italic;font-weight:600;color:var(--teal)}
.btn{position:absolute;display:flex;align-items:center;justify-content:center;background:var(--teal);color:var(--white);font-family:"IBM Plex Mono",monospace;font-size:14px;letter-spacing:.5px}
.rule{position:absolute;width:1px;background:#b9d2cd}
.rule::before{content:"";position:absolute;top:-3px;left:-3px;width:7px;height:7px;border-radius:50%;background:var(--teal)}
.photo{position:absolute}
.arch-frame{position:absolute;border:2px solid var(--teal-soft);border-radius:170px}
.arch-photo{position:absolute;border-radius:160px;overflow:hidden}
.brand{font-family:"Barlow",sans-serif;font-weight:400;color:var(--teal);font-size:22px;letter-spacing:1px}
.band{position:absolute;left:0;width:1200px}
.hero{top:0;height:670px;background:var(--mist)}
.nav a{position:absolute;top:42px;font-family:"Barlow",sans-serif;font-size:15px;color:var(--ink);text-decoration:none;letter-spacing:.5px}
.hero-title{left:125px;top:192px;font-size:54px;color:#4a4a4a;line-height:1.08}
.hero-title span{color:var(--teal);font-weight:400}
.scroll-badge{position:absolute;left:118px;top:540px;width:96px;height:96px;border-radius:50%;border:1px solid var(--teal-soft);display:flex;align-items:center;justify-content:center}
.scroll-badge span{width:60px;height:60px;border-radius:50%;background:var(--teal);display:flex;align-items:center;justify-content:center}
.footer{top:4885px;height:321px;background:var(--sand)}
.foot-head{font-size:18px}
.foot-link{position:absolute;font-family:"Barlow",sans-serif;font-size:14px;color:var(--ink)}
.legal{left:160px;top:5158px;font-family:"Barlow",sans-serif;font-size:12px;color:var(--ink)}
.field-label{position:absolute;font-size:12px;font-weight:500;color:var(--teal)}
.field{position:absolute;height:54px;border:1px solid #d8d8d8;background:var(--white);display:flex;align-items:center;gap:8px;padding-left:16px;font-size:11px;color:#9a9a9a}
</style>
</head>
<body>

<section class="band hero">
  <div class="photo" role="img" aria-label="Smiling woman at a white desk with a pink laptop and a potted plant" style="left:600px;top:95px;width:600px;height:575px;background:linear-gradient(120deg,#eeeeec 0%,#d9c4b4 45%,#e8c6b3 70%,#dfe4dc 100%)"></div>
  <div class="abs brand" style="left:126px;top:36px">PraisewithPellar</div>
  <nav class="nav">
    <a style="left:650px">HOME</a>
    <a style="left:729px">SHOP</a>
    <a style="left:804px">LEARN</a>
  </nav>
  <div class="btn" style="left:890px;top:32px;width:176px;height:42px">Connect With Me</div>
  <h1 class="abs heading hero-title">YOUR SCHOOL<br>CAN <span>ABSOLUTELY<br>THRIVE.</span></h1>
  <div class="rule" style="left:167px;top:406px;height:92px"></div>
  <p class="abs copy" style="left:198px;top:394px;width:385px">Let's partner together to revolutionize your school's culture Into an engaged, high-performing community where everyone belongs.</p>
  <div class="scroll-badge" aria-hidden="true"><span>
    <svg width="20" height="20" viewBox="0 0 20 20"><path d="M4 4 L16 16 M16 8 V16 H8" stroke="#fff" stroke-width="2" fill="none"/></svg>
  </span></div>
</section>

<section class="band" style="top:670px;height:458px"></section>
<div class="band" style="top:1128px;height:697px;background:var(--sand)"></div>

<div class="arch-frame" style="left:175px;top:750px;width:318px;height:485px"></div>
<div class="arch-photo" role="img" aria-label="Young woman in glasses working on a laptop" style="left:190px;top:762px;width:300px;height:460px;background:linear-gradient(160deg,#6d5a4a,#b79d82 45%,#9aa98a 75%,#d9d6cf)"></div>
<h2 class="abs heading" style="left:598px;top:778px;font-size:34px">DIGITAL TOOLS</h2>
<div class="rule" style="left:634px;top:848px;height:92px"></div>
<p class="abs copy" style="left:668px;top:840px;width:340px">From staff and student events, to ___ these digital tools are just one File. Print. away from revolutionizing your school culture. <em>(Printed in color of course) (Get that color ink ready!)</em></p>
<div class="btn" style="left:610px;top:992px;width:230px;height:42px">Explore Digital Tools</div>

<h2 class="abs heading" style="left:144px;top:1345px;font-size:34px">INNOVATICE COURSES</h2>
<div class="rule" style="left:161px;top:1420px;height:115px"></div>
<p class="abs copy" style="left:205px;top:1406px;width:360px">Join an individual or team online training course designed to elevate your leadership skills, revolutionize your school culture or transform student behavior. <em>(And you can even say you thought of it yourself)</em><br>IDK something at the end</p>
<div class="btn" style="left:144px;top:1583px;width:286px;height:42px">Discover Innovative Courses</div>
<div class="arch-frame" style="left:690px;top:1215px;width:330px;height:490px;border-color:#fff"></div>
<div class="arch-photo" role="img" aria-label="Desktop monitor showing a video call grid of educators" style="left:695px;top:1222px;width:315px;height:475px;background:linear-gradient(170deg,#c84a3e,#e4c77d 25%,#4c4c4c 50%,#e6e2da 80%,#cfd6c8)"></div>

<div class="arch-frame" style="left:175px;top:1725px;width:335px;height:485px"></div>
<div class="arch-photo" role="img" aria-label="Hands writing in a planner with colourful sticky notes" style="left:190px;top:1728px;width:318px;height:470px;background:linear-gradient(160deg,#a85a3e,#d9c9b5 45%,#e9d98c 60%,#cfd4dc)"></div>
<h2 class="abs heading" style="left:612px;top:1955px;font-size:34px">AUTHENTIC COACHING</h2>
<div class="rule" style="left:637px;top:2032px;height:70px"></div>
<p class="abs copy" style="left:672px;top:2020px;width:330px">Unleash your leadership potential in this mentorship experience as we work together to curate a personalized plan to <em>(Let's Be Smart Friends!)</em></p>
<div class="btn" style="left:610px;top:2153px;width:205px;height:42px">Start Your Journey</div>

<svg class="abs" style="left:0;top:2290px" width="1200" height="615" viewBox="0 0 1200 615">
  <polygon points="0,0 1200,85 1200,615 0,615" fill="#73a79e"/>
  <polygon points="520,50 1200,45 1200,110" fill="#5b9a8f"/>
</svg>
<h2 class="abs heading" style="left:170px;top:2455px;font-size:34px;color:#fff">YOUR GUIDE TO<br>TRANSFORMATIVE<br>LEADERSHIP</h2>
<p class="abs copy" style="left:170px;top:2595px;width:405px;color:#fff">The most important tool to connect your community and create a high-performing,thriving culture is YOU! Start by unleashing a people-centered leadership style and learn all the #1 Rules to create the culture you dream about by reading an Pagemart #1 New Release <b>Start With Culture.</b></p>
<div class="btn" style="left:170px;top:2782px;width:158px;height:40px;background:var(--teal-deep)">Purchase Book</div>
<div class="photo" role="img" aria-label="Book cover of Start With Culture featuring the author" style="left:690px;top:2450px;width:300px;height:390px;background:linear-gradient(150deg,#f4f2ee,#d6c2ad 50%,#eeeae4);transform:rotate(12deg);box-shadow:0 12px 24px rgba(0,0,0,.2)"></div>

<h2 class="abs heading" style="left:0;width:1200px;top:2985px;font-size:34px;text-align:center">SIGN UP FOR PRAISEWITHPELLAR<br>NEWSLETTER</h2>
<p class="abs" style="left:0;width:1200px;top:3085px;text-align:center;font-style:italic;font-size:17px">(Who doesn't want more emails?)</p>
<div class="field-label" style="left:190px;top:3155px">Full Name</div>
<div class="field" style="left:190px;top:3185px;width:348px"><svg width="12" height="12" viewBox="0 0 12 12"><circle cx="6" cy="4" r="2.5" fill="none" stroke="#999"/><path d="M1.5 11.5c0-2.5 2-4 4.5-4s4.5 1.5 4.5 4" fill="none" stroke="#999"/></svg>Enter your Full Name</div>
<div class="field-label" style="left:555px;top:3155px">Email Address</div>
<div class="field" style="left:555px;top:3185px;width:320px"><svg width="13" height="10" viewBox="0 0 13 10"><rect x=".5" y=".5" width="12" height="9" fill="none" stroke="#999"/><path d="M.5 .5 6.5 5.5 12.5 .5" fill="none" stroke="#999"/></svg>Enter your email</div>
<div class="btn" style="left:892px;top:3185px;width:162px;height:54px">Subscribe</div>

<svg class="abs" style="left:0;top:3315px" width="1200" height="735" viewBox="0 0 1200 735">
  <rect y="40" width="1200" height="695" fill="#f4efe6"/>
  <polygon points="0,0 0,70 330,50" fill="#73a79e"/>
  <polygon points="330,50 1200,30 1200,40 0,70" fill="#5b9a8f" opacity=".35"/>
</svg>
<div class="abs" style="left:155px;top:3375px;width:365px;height:575px;border:2px solid var(--teal-soft);border-radius:182px 182px 0 0"></div>
<div class="arch-photo" role="img" aria-label="Portrait of the author sitting cross-legged in a cream sweater" style="left:175px;top:3385px;width:340px;height:555px;border-radius:170px 170px 0 0;background:linear-gradient(170deg,#f1ece6,#d3b59a 35%,#ece7df 65%,#f7f6f3)"></div>
<h2 class="abs heading" style="left:632px;top:3465px;font-size:34px">MEET ME</h2>
<p class="abs" style="left:632px;top:3522px;font-style:italic;font-weight:600;font-size:13px">(Let's Be Smart Friends!)</p>
<p class="abs copy" style="left:632px;top:3557px;width:380px">Welcome to &nbsp;! I am Pellar Hastings an Elementary Principal in Maplewood, Ohio, Author of Start With Culture, and Education Consultant. I am superpassionate about bringing change to the way school leaders serve -both children and adults.</p>
<p class="abs copy" style="left:632px;top:3717px;width:380px">I was a teacher for eight years, and then an instructional coach, before earning my dream job as an elementary school principal: I am now in my sixth year as a school leader and have dramatically shifted the traditional elementary school culture into a thriving, loving community.</p>
<div class="btn" style="left:632px;top:3898px;width:178px;height:42px">Connect With Me</div>

<svg class="abs" style="left:0;top:4045px" width="1200" height="480" viewBox="0 0 1200 480">
  <polygon points="0,0 1200,0 1200,478 0,375" fill="#73a79e"/>
  <polygon points="330,400 1200,470 1200,478" fill="#5b9a8f"/>
</svg>
<div class="abs" style="left:0;width:1200px;top:4098px;text-align:center;font-family:'Barlow',sans-serif;font-size:110px;line-height:1;color:var(--cream);font-style:italic">&ldquo;</div>
<p class="abs" style="left:240px;width:720px;top:4200px;text-align:center;font-size:22px;line-height:1.75;color:#fff;letter-spacing:.5px">I am so happy you are here! <i style="font-weight:600;color:var(--cream)">(Seriously!)</i> Working with other educational leaders brings me THE.<br>MOST. JOY.<br><i style="color:var(--cream)">(I'm OBSESSED)</i></p>
<div class="abs" role="img" aria-label="Small round portrait of the author" style="left:535px;top:4448px;width:124px;height:124px;border-radius:50%;border:4px solid #fff;background:radial-gradient(circle,#c9a68a,#e9e3db)"></div>
<div class="abs copy" style="left:188px;top:4596px;width:400px;font-size:13px">
  <p>I want to support you on every inch of your journey! We can work alongside each other to navigate the challenges of leading adults, transforming student behaviors, and creating a vibrant atmosphere.</p>
  <p style="margin-top:14px">School leadership can be lonely, taxing, and overwhelming. Often, the biggest challenge isknowing where to start as you face the pressures and demands from the many stakeholders.</p>
</div>
<div class="abs copy" style="left:652px;top:4596px;width:400px;font-size:13px">
  <p>But don't worry, I can't wait to help you!</p>
  <p style="margin-top:14px">So whether you need tools to enhance your own leadership skills, to facilitate connection within your community, or to transform student behaviors, I am here to help you develop your school into a high-performing culture. Let's get started today!!!</p>
</div>
<div class="btn" style="left:514px;top:4808px;width:176px;height:42px">Connect With Me</div>

<footer class="band footer"></footer>
<div class="abs brand" style="left:160px;top:4975px">PraisewithPellar</div>
<h3 class="abs heading foot-head" style="left:568px;top:4935px">NAVIGATION</h3>
<span class="foot-link" style="left:568px;top:4983px">Home</span>
<span class="foot-link" style="left:568px;top:5018px">Shop</span>
<span class="foot-link" style="left:568px;top:5053px">Learn</span>
<span class="foot-link" style="left:653px;top:4983px">Connect with me</span>
<span class="foot-link" style="left:653px;top:5018px">Testimonials</span>
<h3 class="abs heading foot-head" style="left:885px;top:4935px">CONNECT WITH ME</h3>
<svg class="abs" style="left:888px;top:4984px" width="110" height="14" viewBox="0 0 110 14">
  <circle cx="6" cy="7" r="4" fill="#5b9a8f"/>
  <circle cx="33" cy="7" r="4" fill="#5b9a8f"/>
  <circle cx="60" cy="7" r="4" fill="#5b9a8f"/>
  <circle cx="87" cy="7" r="4" fill="#5b9a8f"/>
</svg>
<p class="abs legal">© 2024 All Rights Reserved PraisewithPellar &nbsp;&nbsp;|&nbsp;&nbsp; Privacy Policy &nbsp;&nbsp;|&nbsp;&nbsp; Terms And Condition</p>

</body>
</html>
```